Something that stands out and has more of a modern look to it...will be printing on plastic cards so keep in mind and review old business card as reference

Industry/Entity Type

Real Estate Agent

Contact Information for Business Card

Front of business card will have picture and information the back of card can have logo or name in cursive etc

Logo Text

Marcus Velloran

Font styles to use
Decorative
Script

Colors

Designer to choose colors to be used in the design.

Requirements
Must have
• Must have "Summit 48" logo and state "Bright Harbor Realty Inc Brokerage*" next to it.
• Offices in: Toronto, Markham, Durham
• *Independently Owned and Operated trademarks owned by Summit 48 Real Estate LLC used under license or authorized sub-license. 2017 Summit 48 Canada Limited Partnership. (See old business card for reference)
• Email address: marcus@mvelloranhomes.example
• Website: www.MVelloranHomes.example
• Direct: 647-555-0148
• Name: Marcus Vel Loran
• Office: 905-555-0172
Nice to have
• Maybe a catchy slogan
• One side can have my name designed or the Logo
Should not have
• The Summit 48 Logo too large or focused on (my business requires me just to have this somewhere on the card).
• Yellow and black theme

```html
<!DOCTYPE html>
<html lang="en">
<head>
<meta charset="utf-8">
<title>Marcus Vel Loran – Business Card</title>
<link rel="stylesheet" href="https://fonts.googleapis.com/css2?family=Lobster&family=Montserrat:wght@400;500;700&display=swap">
<style>
  :root {
    --navy: #23253f;
    --navy-light: #34375a;
    --red: #d9232d;
    --white: #ffffff;
    --paper: #f4f4f4;
    --grey: #8a8a8f;
    --bg: #e6e3df;
    --photo-a: #5d6166;
    --photo-b: #2c4a7a;
  }
  * { margin: 0; padding: 0; box-sizing: border-box; }
  html, body { width: 1200px; height: 900px; overflow: hidden; }
  body {
    background: var(--bg);
    font-family: "Montserrat", sans-serif;
    display: flex;
    flex-direction: column;
    align-items: center;
    justify-content: center;
    gap: 40px;
  }
  .card {
    position: relative;
    width: 700px;
    height: 400px;
    overflow: hidden;
    border-radius: 6px;
    box-shadow: 0 6px 18px rgba(0,0,0,.18);
  }

  /* Back side */
  .card-back {
    background: radial-gradient(ellipse at 55% 45%, var(--navy-light), var(--navy) 75%);
    display: flex;
    flex-direction: column;
    align-items: center;
    justify-content: center;
    color: #e9e9ee;
  }
  .card-back .signature {
    font-family: "Lobster", cursive;
    font-size: 64px;
    font-weight: 400;
    letter-spacing: .5px;
  }
  .card-back .slogan {
    margin-top: 8px;
    font-size: 17px;
    letter-spacing: 1px;
  }

  /* Front side */
  .card-front { background: var(--paper); }
  .contact-panel {
    position: absolute;
    left: 380px; top: 172px;
    width: 320px; height: 228px;
    background: var(--navy);
    color: var(--white);
    padding: 40px 20px 0 26px;
    font-size: 14px;
    line-height: 1.55;
  }
  .contact-panel .row { display: flex; align-items: center; gap: 7px; white-space: nowrap; }
  .contact-panel svg { width: 13px; height: 13px; flex: none; }
  .brand-panel {
    position: absolute;
    left: 0; top: 240px;
    width: 380px; height: 160px;
    background: var(--red);
    padding: 34px 30px 0 30px;
    color: var(--white);
  }
  .brokerage-mark { display: flex; align-items: center; justify-content: center; gap: 8px; }
  .brokerage-mark .dot { width: 12px; height: 12px; border-radius: 50%; background: var(--navy); }
  .brokerage-mark .brand-name {
    font-size: 22px; font-weight: 700; color: var(--navy); letter-spacing: -.3px;
  }
  .brokerage-office {
    text-align: center; font-size: 8px; letter-spacing: 1px;
    text-transform: uppercase; color: var(--navy); margin-top: 3px;
  }
  .disclaimer {
    margin-top: 14px; font-size: 8.5px; line-height: 1.45; text-align: center;
  }
  .portrait {
    position: absolute;
    left: 100px; top: 88px;
    width: 150px; height: 150px;
    border-radius: 50%;
    background: linear-gradient(160deg, var(--photo-a) 0%, var(--photo-a) 45%, var(--photo-b) 100%);
  }
  .identity {
    position: absolute;
    left: 262px; top: 52px;
  }
  .identity .name {
    font-family: "Lobster", cursive;
    font-size: 56px;
    font-weight: 400;
    color: var(--red);
    line-height: 1;
    white-space: nowrap;
  }
  .identity .role {
    margin: 6px 0 0 20px;
    font-size: 15px;
    color: var(--grey);
    letter-spacing: 1px;
  }
</style>
</head>
<body>

  <section class="card card-back">
    <h1 class="signature">Marcus Vel Loran</h1>
    <p class="slogan">“First Class Award Winning Service!”</p>
  </section>

  <section class="card card-front">
    <div class="contact-panel">
      <p>Offices in:</p>
      <p>Toronto, Markham, Durham</p>
      <p>Office: 905-555-0172</p>
      <p>Direct: 647-555-0148</p>
      <p class="row">
        <svg viewBox="0 0 16 16" aria-hidden="true"><circle cx="8" cy="8" r="7" fill="#fff"/><path d="M1 8h14M8 1c-3 3.5-3 10.5 0 14M8 1c3 3.5 3 10.5 0 14" stroke="#23253f" stroke-width="1.2" fill="none"/></svg>
        www.MVelloranHomes.example
      </p>
      <p class="row">
        <svg viewBox="0 0 16 16" aria-hidden="true"><rect x="1" y="3" width="14" height="10" fill="none" stroke="#fff" stroke-width="1.4"/><path d="M1 3l7 6 7-6" fill="none" stroke="#fff" stroke-width="1.4"/></svg>
        marcus@mvelloranhomes.example
      </p>
    </div>

    <div class="brand-panel">
      <div class="brokerage-mark">
        <span class="dot"></span>
        <span class="brand-name">Summit 48</span>
      </div>
      <p class="brokerage-office">Bright Harbor Realty Inc Brokerage*</p>
      <p class="disclaimer">*Independently Owned and Operated trademarks owned by Summit 48 Real Estate LLC used under license or authorized sub-license. 2017 Summit 48 Canada Limited Partnership.</p>
    </div>

    <div class="portrait" role="img" aria-label="Portrait photo of Marcus Vel Loran in a blue blazer"></div>

    <div class="identity">
      <h2 class="name">Marcus Vel Loran</h2>
      <p class="role">Sales Representative</p>
    </div>
  </section>

</body>
</html>
```